Marwick Business finance web design

We are a newly established business which provides invoice finance to Small Businesses in England and Wales.
Our approach is very much a funder where the small business owner can talk to the decision maker. We will guarantee on receipt of information, a decision within 24 hours.
We are not a bank so the look of the website need to be friendly but professional.
Have two types of people we are trying to attract to the website: 1) partners who are small business owners and 2) introducers who is accountants and commercial brokers who introduce us to the small businesses.
Currently no website, although domain has been reserved.
The design should be:
Professional
“Clean” Look
Designed to convey Trust and Authority.
Appeal to the small business owner.
Must incorporate:
Logo (attached)
Front page:Top tabs to other pages 1) About us 2) Services 3) Introducers 4) Contact us
Need picture and logo on page.
1) About us page- Room for talk about the company, the people and our critera.
2) Services page- We need for what invoice finance is, and 5 boxes for different services we will provide. (link on page to contact us)
3) Introducers page- We need a part for why become an introducer? Who we can help? Why we are different? (link on page to contact us)
4) Contact us page- Office address, email, tel and if possible a map and a contact me part which will email direct to us.
Text will be provided for the design, if we can see the setup of the website we will provide a part for each of the pages to support.
Styles we think convey the correct image:
www.tovelfunding.example
www.brimsorkfs.example
www.plyfunding.example
Target Market(s)
Small business owners
Industry/Entity Type
Finance
Number of Pages Required
5+ page
Look and feel

```html
<!DOCTYPE html>
<html lang="en">
<head>
<meta charset="utf-8">
<title>Marwick Business finance</title>
<link rel="stylesheet" href="https://fonts.googleapis.com/css2?family=Arimo:wght@400;700&family=Roboto:wght@300;400&family=Open+Sans:wght@400;600&display=swap">
<style>
  :root {
    --red: #e2363c;
    --red-dark: #d32f35;
    --charcoal: #333333;
    --ink: #1d1d1d;
    --white: #ffffff;
    --muted: #e9e9e9;
    --hero-deep: #1b2b45;
    --hero-mid: #3d5f86;
    --hero-light: #8ba7c4;
  }
  * { box-sizing: border-box; margin: 0; padding: 0; }
  html, body { width: 1200px; height: 2586px; overflow: hidden; }
  body {
    position: relative;
    background: var(--white);
    font-family: "Arimo", Arial, sans-serif;
    color: var(--ink);
  }
  .abs { position: absolute; }

  /* top contact bar */
  .topbar { left: 0; top: 0; width: 1200px; height: 45px; background: var(--red); color: var(--white); font-size: 15px; }
  .topbar .item { position: absolute; top: 14px; display: flex; align-items: center; gap: 10px; }

  /* navigation */
  .nav { left: 0; top: 45px; width: 1200px; height: 79px; background: var(--white); }
  .nav a { position: absolute; top: 31px; font-size: 16px; color: var(--ink); text-decoration: none; letter-spacing: .5px; }
  .brand { position: absolute; left: 0; width: 1200px; top: 16px; text-align: center; font-family: "Arimo", Arial, sans-serif; font-weight: 700; font-size: 38px; color: var(--red); pointer-events: none; }

  /* hero */
  .hero { left: 0; top: 124px; width: 1200px; height: 609px;
    background: linear-gradient(115deg, var(--hero-deep) 0%, var(--hero-mid) 45%, var(--hero-light) 75%, #4a5d75 100%); }
  .hero-title { left: 0; top: 510px; width: 1200px; text-align: center; color: var(--white);
    font-family: "Roboto", Arial, sans-serif; font-weight: 300; font-size: 72px; line-height: 72px; letter-spacing: 2px; z-index: 2; }
  .hero-tag { left: 281px; top: 686px; width: 636px; height: 79px; background: var(--white);
    box-shadow: 4px 4px 6px rgba(0,0,0,.45); display: flex; align-items: center; justify-content: center;
    font-family: "Arimo", Arial, sans-serif; font-size: 34px; line-height: 1; color: var(--ink); letter-spacing: .5px; z-index: 5; }

  /* service strip */
  .services { left: 0; top: 733px; width: 1200px; height: 363px; background: var(--charcoal); z-index: 1; }
  .service { position: absolute; top: 66px; width: 300px; text-align: center; color: var(--white); }
  .service h3 { font-weight: 400; font-size: 20px; letter-spacing: .5px; }
  .service .icon { margin: 30px auto 0; width: 58px; height: 58px; display: block; }
  .service p { margin-top: 28px; font-size: 13.5px; line-height: 16px; }

  /* feature rows */
  .photo { border-radius: 2px; }
  .feature h2 { font-family: "Arimo", Arial, sans-serif; font-weight: 400; color: var(--red); font-size: 22px; line-height: 27px; letter-spacing: .6px; }
  .feature p { margin-top: 18px; font-size: 13.4px; line-height: 21px; text-align: justify; color: var(--ink); }
  .btn { position: absolute; background: var(--red); color: var(--white); border-radius: 5px; font-size: 13px; text-decoration: none;
    display: flex; align-items: center; justify-content: center; box-shadow: 0 2px 3px rgba(0,0,0,.25); }

  /* fitness band */
  .fitness { left: 0; top: 1883px; width: 1200px; height: 244px; background: var(--red); color: var(--white); }
  .fitness h2 { position: absolute; top: 22px; left: 0; width: 1200px; text-align: center; font-family: "Open Sans", Arial, sans-serif; font-weight: 400; font-size: 26px; }
  .tool { position: absolute; top: 88px; width: 180px; text-align: center; font-family: "Open Sans", Arial, sans-serif; font-size: 17px; line-height: 21px; }
  .tool svg { display: block; margin: 0 auto 18px; width: 54px; height: 54px; }

  /* footer info */
  .info { left: 0; top: 2127px; width: 1200px; height: 407px; background: var(--charcoal); color: var(--white); }
  .info-col { position: absolute; top: 80px; text-align: center; }
  .info-col h3 { font-family: "Open Sans", Arial, sans-serif; font-weight: 400; font-size: 22px; line-height: 27px; }
  .info-col p { margin-top: 20px; font-size: 13.4px; line-height: 17px; }

  .footbar { left: 0; top: 2534px; width: 1200px; height: 52px; background: var(--red); color: var(--white); font-size: 13px; display: flex; align-items: center; justify-content: center; }
</style>
</head>
<body>

<header class="abs topbar">
  <div class="item" style="left:56px">
    <svg width="16" height="16" viewBox="0 0 24 24" aria-hidden="true"><path fill="#fff" d="M6.6 10.8a15.1 15.1 0 0 0 6.6 6.6l2.2-2.2c.3-.3.7-.4 1-.2 1.1.4 2.3.6 3.6.6.6 0 1 .4 1 1V20c0 .6-.4 1-1 1A17 17 0 0 1 3 4c0-.6.4-1 1-1h3.5c.6 0 1 .4 1 1 0 1.3.2 2.5.6 3.6.1.3 0 .7-.2 1z"/></svg>
    <span>555.014.2287</span>
  </div>
  <div class="item" style="left:190px">
    <svg width="18" height="14" viewBox="0 0 18 14" aria-hidden="true"><rect x="1" y="1" width="16" height="12" fill="none" stroke="#fff" stroke-width="1.6"/><path d="M1 1l8 6 8-6" fill="none" stroke="#fff" stroke-width="1.6"/></svg>
    <span>hello@marwickfinance.example</span>
  </div>
</header>

<nav class="abs nav">
  <a href="#" style="left:150px">ABOUT US</a>
  <a href="#" style="left:345px">SERVICES</a>
  <div class="brand">Marwick</div>
  <a href="#" style="left:731px">INTRODUCERS</a>
  <a href="#" style="left:932px">CONTACT US</a>
</nav>

<section class="abs hero" role="img" aria-label="Businessman drawing a glowing rising line chart on a transparent screen"></section>
<h1 class="abs hero-title">Improve Your Business<br>Cash Flow Fast</h1>

<section class="abs services">
  <div class="service" style="left:56px">
    <h3>FINANCIAL PLANNING</h3>
    <svg class="icon" viewBox="0 0 58 58" aria-hidden="true"><circle cx="29" cy="29" r="27" fill="none" stroke="#fff" stroke-width="2"/><circle cx="29" cy="19" r="4" fill="#fff"/><path d="M25 25h8l-1 9-1 10h-4l-1-10z" fill="#fff"/></svg>
    <p>There are many variations of passages of Lorem Ipsum available, but the majority have suffered alteration in some form, by injected humour, or randomised words which don't look even slightly believable.</p>
  </div>
  <div class="service" style="left:450px">
    <h3>BONDS</h3>
    <svg class="icon" viewBox="0 0 58 58" aria-hidden="true"><circle cx="29" cy="29" r="27" fill="none" stroke="#fff" stroke-width="2"/><path d="M19 27h5v13h-5zM26 27l5-9c2 0 3 1 3 3l-1 5h7c2 0 3 2 2 4l-3 9c0 1-1 1-2 1H26z" fill="none" stroke="#fff" stroke-width="2" stroke-linejoin="round"/></svg>
    <p>There are many variations of passages of Lorem Ipsum available, but the majority have suffered alteration in some form, by injected humour, or randomised words which don't look even slightly believable.</p>
  </div>
  <div class="service" style="left:845px">
    <h3>RETIREMENT</h3>
    <svg class="icon" viewBox="0 0 58 58" aria-hidden="true"><circle cx="29" cy="29" r="27" fill="none" stroke="#fff" stroke-width="2"/><path d="M20 38l2-7 13-13 5 5-13 13zM32 21l5 5" fill="none" stroke="#fff" stroke-width="2" stroke-linejoin="round"/></svg>
    <p>There are many variations of passages of Lorem Ipsum available, but the majority have suffered alteration in some form, by injected humour, or randomised words which don't look even slightly believable.</p>
  </div>
</section>

<div class="abs hero-tag">WE OFFER FINANCING SOLUTIONS</div>

<div class="abs photo" role="img" aria-label="Figure running up rising bar chart towards a green dollar sign" style="left:52px;top:1112px;width:448px;height:284px;background:linear-gradient(135deg,#f4f7fb 0%,#e3eef6 45%,#f3c892 70%,#7cc46a 100%)"></div>
<article class="abs feature" style="left:583px;top:1134px;width:550px">
  <h2>HOW INVOICE FACTORING WORKS FREQUENTLY ASKED QUESTIONS FROM INVOICING TOH COLLECTION</h2>
  <p>It is a long established fact that a reader will be distracted by the readable content of a page when looking at its layout. The point of using Lorem Ipsum is that it has a more-or-less normal distribution of letters, as opposed to using 'Content here, content here', making it look like readable English. Many desktop publishing packages and web page editors now use Lorem Ipsum as their default model text, and a search for 'lorem ipsum' will uncover many web sites still in their infancy. Various versions have evolved over the years, sometimes by accident, sometimes on purpose (injected humour and the like).</p>
</article>
<a class="btn" href="#" style="left:583px;top:1419px;width:226px;height:34px">How Invoice Factoring Works</a>

<article class="abs feature" style="left:57px;top:1508px;width:524px">
  <h2 style="text-align:center">OFFERS FROM FACTORING COMPANIES WHAT DEALS ARE REALISTIC FOR YOUR BUSINESS?</h2>
  <p>There are many variations of passages of Lorem Ipsum available, but the majority have suffered alteration in some form, by injected humour, or randomised words which don't look even slightly believable. If you are going to use a passage of Lorem Ipsum, you need to be sure there isn't anything embarrassing hidden in the middle of text. All the Lorem Ipsum generators on the Internet tend to repeat predefined chunks as necessary, making this the first true generator on the Internet. It uses a dictionary of over 200 Latin words, combined with a handful of model sentence structures.</p>
</article>
<a class="btn" href="#" style="left:55px;top:1772px;width:228px;height:38px">How Invoice Factoring Works</a>
<div class="abs photo" role="img" aria-label="Hand placing a coin on a pile of coins with a green sprout growing" style="left:664px;top:1469px;width:477px;height:289px;background:radial-gradient(ellipse at 35% 60%,#6fae3a 0%,#b99a5a 35%,#efe6d6 65%,#ffffff 85%)"></div>

<section class="abs fitness">
  <h2>Improve your business with our free Business Financial Fitness Program</h2>
  <div class="tool" style="left:1px">
    <svg viewBox="0 0 54 54" aria-hidden="true"><g fill="#fff"><circle cx="27" cy="27" r="15"/><rect x="23" y="4" width="8" height="46" rx="2"/><rect x="4" y="23" width="46" height="8" rx="2"/><rect x="23" y="4" width="8" height="46" rx="2" transform="rotate(45 27 27)"/><rect x="23" y="4" width="8" height="46" rx="2" transform="rotate(-45 27 27)"/></g><circle cx="27" cy="27" r="6" fill="#e2363c"/></svg>
    Financial<br>Tools
  </div>
  <div class="tool" style="left:225px">
    <svg viewBox="0 0 54 54" aria-hidden="true"><rect x="5" y="16" width="44" height="30" rx="3" fill="none" stroke="#fff" stroke-width="3"/><path d="M20 16v-5h14v5M5 28h44" fill="none" stroke="#fff" stroke-width="3"/><rect x="24" y="25" width="6" height="7" fill="#fff"/></svg>
    Management<br>Lessons
  </div>
  <div class="tool" style="left:491px">
    <svg viewBox="0 0 54 54" aria-hidden="true"><g fill="#fff"><circle cx="27" cy="13" r="7"/><path d="M17 34c0-8 4-12 10-12s10 4 10 12z"/><circle cx="14" cy="27" r="6"/><path d="M5 46c0-7 4-11 9-11s9 4 9 11z"/><circle cx="40" cy="27" r="6"/><path d="M31 46c0-7 4-11 9-11s9 4 9 11z"/></g></svg>
    Quizzes
  </div>
  <div class="tool" style="left:739px">
    <svg viewBox="0 0 54 54" aria-hidden="true"><g stroke="#fff" stroke-width="2"><path d="M27 27L27 7M27 27L27 47M27 27L7 27M27 27L47 27M27 27L13 13M27 27L41 13M27 27L13 41M27 27L41 41"/></g><g fill="#fff"><circle cx="27" cy="27" r="7"/><circle cx="27" cy="6" r="4"/><circle cx="27" cy="48" r="4"/><circle cx="6" cy="27" r="4"/><circle cx="48" cy="27" r="4"/><circle cx="12" cy="12" r="3.5"/><circle cx="42" cy="12" r="3.5"/><circle cx="12" cy="42" r="3.5"/><circle cx="42" cy="42" r="3.5"/></g></svg>
    Blogs
  </div>
  <div class="tool" style="left:982px">
    <svg viewBox="0 0 54 54" aria-hidden="true"><path d="M10 38A22 22 0 1 1 40 45" fill="none" stroke="#fff" stroke-width="3"/><rect x="28" y="6" width="16" height="11" rx="2" fill="#fff"/><rect x="14" y="26" width="14" height="10" rx="2" fill="#fff"/><circle cx="36" cy="30" r="4" fill="#fff"/><path d="M29 42c0-5 3-7 7-7s7 2 7 7z" fill="#fff"/></svg>
    A&amp;Z Community
  </div>
</section>

<footer class="abs info">
  <div class="info-col" style="left:44px;width:280px">
    <h3>About Invoice Factoring<br>Companies</h3>
    <p style="text-align:left;padding:0 10px">It is a long established fact that a reader will be distracted by the readable content of a page when looking at its layout. The point of using Lorem Ipsum is that it has a more-or-less normal distribution of letters, as opposed to using 'Content here, content here', making it look like readable English.</p>
  </div>
  <div class="info-col" style="left:431px;width:280px">
    <h3>About Our Commercial<br>Finance Companies</h3>
    <p style="padding:0 20px">Contrary to popular belief, Lorem Ipsum is not simply random text. It has roots in a piece of classical Latin literature from 45 BC, making it over 2000 years old. Edwin Halloway.</p>
  </div>
  <div class="info-col" style="left:816px;width:340px;top:74px">
    <h3>Our Affiliations &amp; Partnerships</h3>
  </div>
  <div class="abs" role="img" aria-label="Tablet showing a colourful 3D bar chart with a rising trend arrow" style="left:858px;top:128px;width:292px;height:185px;background:linear-gradient(160deg,#5b8fd6 0%,#c9ccd1 40%,#f08a2a 70%,#e9e9e9 100%);border-radius:6px"></div>
</footer>

<div class="abs footbar">office@marwickfinance.example 2016</div>

</body>
</html>
```